Zorveli Foods Web Page Templates

I need two templates designed for a wholesale food/catering business, one template for the home page and the other for detail pages. The overall template should be a simple, clean and clear design. I have provided the existing logo to which the templates should directly relate.
Zorveli Foods supplies food based upon traditional Ghanian recipes to a number of stores across Canberra. In addition, Zorveli Foods offers catering for public and private functions across the Canberra region.
The colours in the logo represent the national colours of Ghana (yellow, green, red and black) and the website content will also include traditional Ghanian Kente patterns which will add further colour elements to the site. On this basis, the template design needs to be fairly sparse so as not to compete with the colourful content of the website detail pages.
There is no requirement for specific pages to be designed, as these will be handled in the CMS implementation.
The information provided in the Word document is only designed to provide a sense of the intended content of the website, not as a requirement for specific pages to be produced.

Target Market(s)

Retail/Wholesale food

Number of Pages Required

2 page

Font styles to use
Serif

Colors

Designer to choose colors to be used in the design.

Requirements
Must have
• Template must accommodate a responsive design
• The logo provided will form the cornerstone of the design
Nice to have
• There
Should not have
• Please do not solicit for extra work or for alternative logo design.

```html
<!DOCTYPE html>
<html lang="en">
<head>
<meta charset="utf-8">
<title>Zorveli Foods — Home</title>
<link href="https://fonts.googleapis.com/css2?family=Playfair+Display:wght@400;700&family=Great+Vibes&family=Montserrat:wght@400;500;600&display=swap" rel="stylesheet">
<style>
:root{
  --accent:#ee6a45;
  --ink:#222222;
  --muted:#555555;
  --white:#ffffff;
  --footer:#1e1e1e;
  --footer-deep:#151515;
  --gold:#e9b52f;
  --grey-text:#8a8a8a;
}
*{margin:0;padding:0;box-sizing:border-box}
html,body{width:1200px;height:4283px;overflow:hidden;background:var(--white)}
body{position:relative;font-family:"Montserrat",sans-serif;color:var(--ink)}
section,header,footer{position:absolute;left:0;width:1200px}
h1,h2,h3{font-weight:400}
.abs{position:absolute}
.center{text-align:center}
.script{font-family:"Great Vibes",cursive;color:var(--accent);font-size:70px;line-height:1;font-weight:400}
.serif-title{font-family:"Playfair Display",serif;font-weight:400;font-size:27px;letter-spacing:.3px;color:var(--ink);text-transform:uppercase;line-height:33px}
.body-copy{font-size:11.5px;line-height:21px;color:var(--muted)}
.text-link{font-size:12px;font-weight:600;color:var(--accent);text-decoration:underline}
.photo{position:absolute}

/* Hero */
.hero{top:0;height:585px;overflow:hidden;background:radial-gradient(ellipse 70% 80% at 45% 45%,#f0e6d2 0%,#d6c09a 30%,#a4805a 60%,#6e4a30 85%,#8a2a1e 100%)}
.hero::after{content:"";position:absolute;inset:0;background:linear-gradient(180deg,rgba(0,0,0,.28),rgba(0,0,0,.18) 60%,rgba(0,0,0,.3))}
.nav{position:absolute;top:56px;left:0;width:1200px;z-index:2;font-size:11.5px;font-weight:500;color:var(--white)}
.nav span{position:absolute;transform:translateX(-50%)}
.nav .active{color:var(--accent)}
.nav .brand{font-size:20px;top:-8px;color:var(--gold);font-weight:500;white-space:nowrap}
.hero-welcome{position:absolute;left:0;width:1200px;top:208px;z-index:2;font-size:80px}
.hero-title{position:absolute;left:0;width:1200px;top:275px;font-family:"Playfair Display",serif;font-weight:700;font-size:80px;line-height:100px;color:var(--white);z-index:2;letter-spacing:1px}
.hero-sub{position:absolute;left:0;width:1200px;top:366px;z-index:2;font-size:18px;font-weight:600;letter-spacing:3px;color:var(--white)}
.arrow{position:absolute;top:272px;z-index:2}

/* Menu */
.menu{top:585px;height:445px}
.tile{position:absolute;top:156px;width:203px;height:203px;display:flex;align-items:center;justify-content:center;text-align:center;font-family:"Playfair Display",serif;font-weight:700;font-size:20px;line-height:23px;color:var(--white);text-shadow:0 1px 4px rgba(0,0,0,.5)}

/* Story */
.story{top:1030px;height:438px;background:radial-gradient(ellipse 45% 70% at 25% 55%,#efe4da 0%,#f8f4f0 55%,#ffffff 100%)}

/* Booking */
.booking{top:1468px;height:487px;overflow:hidden;background:radial-gradient(ellipse 55% 75% at 58% 50%,#f2d99a 0%,#d9b26a 35%,#9c7446 65%,#4a3322 100%)}
.booking::after{content:"";position:absolute;inset:0;background:rgba(0,0,0,.22)}

/* Event */
.event{top:1955px;height:497px}

/* Gallery */
.gallery{top:2452px;height:560px;background:radial-gradient(ellipse 60% 70% at 50% 50%,#ece6df 0%,#cdb9a6 50%,#8e6a52 100%)}
.gallery-photo{position:absolute;top:204px;width:276px;height:261px;border:3px solid var(--white)}

/* Testimonials */
.testimonials{top:3012px;height:495px;background:linear-gradient(90deg,#ffffff 55%,#f4ebe2 80%,#efe2d4 100%)}
.dots span{display:inline-block;width:6px;height:6px;border-radius:50%;background:#cfcfcf;margin:0 3px}

/* Map */
.map{top:3507px;height:329px;background:radial-gradient(ellipse 70% 90% at 45% 50%,#e2e2e2 0%,#d2d2d2 60%,#bdbdbd 100%)}

/* Footer */
.contact-band{top:3836px;height:199px;background:var(--footer)}
.contact-col{position:absolute;top:58px;width:280px;transform:translateX(-50%);text-align:center}
.contact-col h3{font-family:"Playfair Display",serif;font-weight:400;font-size:23px;color:var(--white);letter-spacing:.5px}
.contact-col p{font-size:13px;line-height:19px;color:var(--grey-text);margin-top:8px;text-transform:uppercase}
.socials{margin-top:10px;display:flex;gap:8px;justify-content:center}
.socials span{width:23px;height:23px;border:2px solid var(--white);border-radius:50%}
.base{top:4035px;height:248px;background:var(--footer-deep)}
.base-brand{position:absolute;top:38px;left:0;width:1200px;text-align:center;font-size:40px;font-weight:500;color:var(--gold);letter-spacing:2px}
.base-nav{position:absolute;top:127px;left:0;width:1200px;text-align:center;font-size:11.5px;color:#9a9a9a}
.base-nav span{margin:0 11px}
.base-rule{position:absolute;top:187px;left:165px;width:870px;height:1px;background:#2c2c2c}
.copyright{position:absolute;top:209px;left:0;width:1200px;text-align:center;font-size:10px;color:#5c5c5c}
</style>
</head>
<body>

<header class="hero">
  <div class="photo" role="img" aria-label="Close-up of a baked chicken and rice casserole" style="inset:0"></div>
  <nav class="nav">
    <span class="active" style="left:316px">HOME</span>
    <span style="left:389px">ABOUT US</span>
    <span style="left:469px">EVENTS</span>
    <span class="brand" style="left:598px">Zorveli Foods</span>
    <span style="left:745px">GALLERY</span>
    <span style="left:814px">MENU</span>
    <span style="left:888px">CONTACT</span>
  </nav>
  <svg class="arrow" style="left:62px" width="24" height="40" viewBox="0 0 24 40"><path d="M20 2 L4 20 L20 38" fill="none" stroke="#fff" stroke-width="2.5"/></svg>
  <svg class="arrow" style="left:1112px" width="24" height="40" viewBox="0 0 24 40"><path d="M4 2 L20 20 L4 38" fill="none" stroke="#fff" stroke-width="2.5"/></svg>
  <div class="script hero-welcome center">Welcome To</div>
  <h1 class="hero-title center">ZORVELI FOODS</h1>
  <div class="hero-sub center">HAVE A TASTE! ENJOY!!</div>
  <svg class="abs" style="left:395px;top:377px;z-index:2" width="410" height="2"><line x1="0" y1="1" x2="65" y2="1" stroke="#fff" stroke-opacity=".6"/><line x1="345" y1="1" x2="410" y2="1" stroke="#fff" stroke-opacity=".6"/></svg>
</header>

<section class="menu">
  <div class="script abs center" style="top:40px;width:1200px">Menu</div>
  <h2 class="serif-title abs center" style="top:104px;width:1200px">Food &amp; Catering</h2>
  <div class="tile" role="img" aria-label="Chicken casserole dish" style="left:165px;background:radial-gradient(ellipse at 40% 40%,#d9b27a,#8a6238 70%,#4e3a2a)">Chicken<br>Casserole</div>
  <div class="tile" role="img" aria-label="Spicy beef casserole in a white bowl" style="left:389px;background:radial-gradient(ellipse at 50% 45%,#8a4a26,#4a3426 60%,#8a8a88)">Spicy Beef<br>Casserole</div>
  <div class="tile" role="img" aria-label="Black-eyed beans casserole" style="left:615px;background:radial-gradient(ellipse at 50% 55%,#b0582e,#6a4632 60%,#2e2620)">Black-eyed<br>Beans Casserole</div>
  <div class="tile" role="img" aria-label="Ghanaian chilli sauce in a jar" style="left:831px;background:radial-gradient(ellipse at 35% 40%,#8a2e3a,#7a5a66 55%,#b8a2a8)">Ghanaian<br>Chilli Sauce</div>
  <a class="text-link abs center" style="top:389px;width:1200px">View More</a>
</section>

<section class="story">
  <div class="script abs center" style="top:48px;left:116px;width:500px">Our Story</div>
  <h2 class="serif-title abs center" style="top:110px;left:116px;width:500px">The Great Story Of</h2>
  <h2 class="serif-title abs center" style="top:143px;left:116px;width:500px;color:var(--accent)">Zorveli Foods</h2>
  <p class="body-copy abs center" style="top:182px;left:176px;width:380px">Lorem ipsum dolor sit amet, consectetur adipisicing elit, sed do eiusmod tempor incididunt ut labore et dolore magna aliqua. Ut enim ad minim veniam, quis nostrud exercitation ullamco laboris nisi ut aliquip ex ea commodo consequat. Duis aute irure dolor in reprehenderit in voluptate velit esse cillum dolore.</p>
  <a class="text-link abs center" style="top:307px;left:116px;width:500px">Read More</a>
  <div class="photo" role="img" aria-label="Bowl of red chilli sauce with a spoon" style="left:615px;top:42px;width:203px;height:309px;background:radial-gradient(ellipse at 50% 65%,#9a2a1a,#7a5a3e 45%,#4a3a2c)"></div>
  <div class="photo" role="img" aria-label="Bowl of beef stew on stacked plates" style="left:831px;top:42px;width:203px;height:309px;background:radial-gradient(ellipse at 50% 42%,#6a3a22,#3a3a2a 45%,#9aa0a4 80%,#d8d8d8)"></div>
</section>

<section class="booking">
  <div class="photo" role="img" aria-label="Baked pasta with broccoli and cheese beside a spoon" style="inset:0"></div>
  <div class="script abs center" style="top:160px;width:1200px;z-index:2">Booking</div>
  <h2 class="abs center" style="top:252px;width:1200px;z-index:2;font-family:'Playfair Display',serif;font-weight:400;font-size:48px;color:var(--white)">BOOK NOW</h2>
</section>

<section class="event">
  <div class="photo" role="img" aria-label="Plates of noodles and spring rolls with chillies" style="left:0;top:23px;width:400px;height:415px;background:radial-gradient(ellipse at 35% 50%,#d99a5a 0%,#ecd2b0 40%,#ffffff 75%)"></div>
  <div class="photo" role="img" aria-label="Bowls of spices and a small pan of chillies" style="left:922px;top:40px;width:278px;height:400px;background:radial-gradient(ellipse at 55% 50%,#d9783a 0%,#efc9a8 40%,#ffffff 75%)"></div>
  <div class="script abs center" style="top:120px;width:1400px;left:0">Event</div>
  <h2 class="serif-title abs center" style="top:178px;left:0;width:1400px">Private Dining<br>&amp; Events</h2>
  <p class="body-copy abs center" style="top:275px;left:510px;width:380px">Lorem ipsum dolor sit amet, consectetur adipisicing elit, sed do eiusmod tempor incididunt ut labore et dolore magna aliqua. Ut enim ad minim veniam, quis nostrud exercitation ullamco laboris nisi ut aliquip ex ea commodo consequat. Duis aute irure dolor in reprehenderit in voluptate velit esse cillum dolore.</p>
  <a class="text-link abs center" style="top:397px;left:0;width:1400px">VIEW EVENTS</a>
</section>

<section class="gallery">
  <div class="photo" role="img" aria-label="Blurred background of a meat and vegetable stew" style="inset:0;background:rgba(255,255,255,.35)"></div>
  <div class="script abs center" style="top:55px;width:1200px">Gallery</div>
  <h2 class="abs center" style="top:132px;width:1200px;font-family:'Playfair Display',serif;font-weight:400;font-size:46px;color:var(--ink)">OUR GALLERY</h2>
  <div class="gallery-photo" role="img" aria-label="Baked pasta with broccoli" style="left:161px;background:radial-gradient(ellipse at 50% 45%,#f2d27a,#d6a84a 55%,#8a6a2e)"></div>
  <div class="gallery-photo" role="img" aria-label="Beef and bean stew with herbs" style="left:462px;background:radial-gradient(ellipse at 50% 50%,#7a3e2a,#4a2a1e 60%,#d8d2cc)"></div>
  <div class="gallery-photo" role="img" aria-label="Vegetable soup in a white bowl" style="left:761px;background:radial-gradient(circle,#d8602a 40%,#f0ece4 70%,#7aa84a)"></div>
  <a class="text-link abs center" style="top:496px;width:1200px;color:var(--ink)">VIEW More</a>
</section>

<section class="testimonials">
  <div class="photo" role="img" aria-label="Smiling chef in white uniform with arms crossed" style="left:0;top:71px;width:241px;height:424px;background:linear-gradient(180deg,#fafafa,#ececec 55%,#dcdcdc 85%,#2a2a2a)"></div>
  <div class="script abs center" style="top:60px;width:1200px">Testimonials</div>
  <h2 class="serif-title abs center" style="top:120px;width:1200px">Reviews From Customers</h2>
  <div class="photo" role="img" aria-label="Customer portrait" style="left:554px;top:186px;width:92px;height:92px;border-radius:50%;background:radial-gradient(circle,#f6e2d4,#e8c2a8)"></div>
  <div class="abs" style="left:620px;top:218px;font-family:'Playfair Display',serif;font-weight:700;font-size:80px;line-height:1;color:var(--accent)">&rdquo;</div>
  <p class="body-copy abs center" style="top:309px;left:250px;width:700px">Lorem ipsum dolor sit amet, consectetur adipisicing elit, sed do eiusmod tempor incididunt ut labore et dolore magna aliqua. Ut enim ad minim veniam, quis nostrud exercitation ullamco laboris nisi ut aliquip ex ea commodo consequat. Duis aute irure dolor in reprehenderit in voluptate velit esse cillum dolore.</p>
  <a class="text-link abs center" style="top:390px;width:1200px">Efua Mensah</a>
  <div class="dots abs center" style="top:432px;width:1200px"><span></span><span></span><span></span></div>
</section>

<section class="map" role="img" aria-label="Street map of the business location"></section>

<footer class="contact-band">
  <div class="contact-col" style="left:307px"><h3>ADDRESS</h3><p>14 Harbour Lane,<br>Canberra</p></div>
  <div class="contact-col" style="left:600px"><h3>FOLLOW US</h3><div class="socials"><span></span><span></span><span></span><span></span></div></div>
  <div class="contact-col" style="left:894px"><h3>CONTACT US</h3><p>hello@zorvelifoods.com<br>+61 2 5550 1947</p></div>
</footer>

<footer class="base">
  <div class="base-brand">Zorveli Foods</div>
  <nav class="base-nav"><span>HOME</span><span>ABOUT US</span><span>EVENTS</span><span>GALLERY</span><span>MENU</span><span>CONTACT</span></nav>
  <div class="base-rule"></div>
  <div class="copyright">© 2019 Zorveli Foods · All Rights Reserved</div>
</footer>

</body>
</html>
```